Save the date for wedding

A save the date for our wedding. We're looking for a simple and sleek invite. I would prefer not alot of calligraphy. Minimalism is good. The basic info to include is as follows:
Names: Mona and Felix
Date: June 9th
Where: Ottawa, Ontario
In small print please include that there will be a reception in Edmonton AB September 1st for those who cannot make it to Ottawa.
Please see the attached file for a style idea. Doesn’t have to be exactly like that, but something like that.

```html
<!DOCTYPE html>
<html lang="en">
<head>
<meta charset="utf-8">
<title>Save the Date – Mona and Felix</title>
<link rel="stylesheet" href="https://fonts.googleapis.com/css2?family=Allura&family=Quicksand:wght@300;400;600;700&display=swap">
<style>
  :root {
    --paper: #f4f4ef;
    --card: #ffffff;
    --olive: #7b8150;
    --olive-soft: #8a8f62;
    --rose: #e9507c;
    --rose-soft: #f3a3b4;
    --leaf: #8fb14a;
    --shadow: rgba(120, 125, 90, 0.22);
  }
  * { box-sizing: border-box; margin: 0; padding: 0; }
  html, body {
    width: 1200px;
    height: 857px;
    overflow: hidden;
    background: var(--paper);
  }
  .canvas {
    position: relative;
    width: 1200px;
    height: 857px;
    overflow: hidden;
    background: var(--paper);
    font-family: "Quicksand", sans-serif;
  }
  .floral-border {
    position: absolute;
    inset: 0;
    background:
      radial-gradient(ellipse 700px 130px at 50% 0%, rgba(233, 80, 124, 0.28), transparent 75%),
      radial-gradient(ellipse 700px 130px at 50% 100%, rgba(233, 80, 124, 0.28), transparent 75%),
      radial-gradient(ellipse 120px 420px at 0% 50%, rgba(143, 177, 74, 0.30), transparent 80%),
      radial-gradient(ellipse 120px 420px at 100% 50%, rgba(233, 80, 124, 0.26), transparent 80%),
      var(--paper);
  }
  .card {
    position: absolute;
    left: 182px;
    top: 138px;
    width: 836px;
    height: 579px;
    background: var(--card);
    border-radius: 42px;
    box-shadow: 0 4px 14px var(--shadow);
  }
  .headline {
    position: absolute;
    left: 0;
    top: 0;
    width: 100%;
    height: 230px;
    font-family: "Allura", cursive;
    color: var(--olive);
  }
  .headline .save {
    position: absolute;
    left: 228px;
    top: 10px;
    font-size: 104px;
    line-height: 1;
  }
  .headline .the {
    position: absolute;
    left: 352px;
    top: 116px;
    font-size: 42px;
    line-height: 1;
    color: var(--olive-soft);
  }
  .headline .date {
    position: absolute;
    left: 392px;
    top: 96px;
    font-size: 110px;
    line-height: 1;
  }
  .tagline {
    position: absolute;
    left: 0;
    width: 100%;
    top: 210px;
    text-align: center;
    font-size: 27px;
    font-weight: 400;
    letter-spacing: 2px;
    color: var(--olive-soft);
  }
  .couple {
    position: absolute;
    left: 0;
    width: 100%;
    top: 288px;
    text-align: center;
    font-size: 42px;
    font-weight: 400;
    letter-spacing: 1px;
    color: var(--rose);
  }
  .couple .joiner {
    font-size: 32px;
    color: var(--olive);
  }
  .when {
    position: absolute;
    left: 0;
    width: 100%;
    top: 390px;
    text-align: center;
    font-size: 24px;
    font-weight: 700;
    letter-spacing: 1px;
    color: var(--olive);
  }
  .when sup { font-size: 11px; vertical-align: 11px; }
  .where {
    position: absolute;
    left: 0;
    width: 100%;
    top: 424px;
    text-align: center;
    font-size: 24px;
    font-weight: 300;
    letter-spacing: 2px;
    color: var(--olive);
  }
  .divider {
    position: absolute;
    left: 118px;
    top: 482px;
    width: 600px;
    height: 1.5px;
    background: var(--olive);
  }
  .note {
    position: absolute;
    left: 0;
    width: 100%;
    top: 503px;
    text-align: center;
    font-size: 18px;
    font-weight: 700;
    line-height: 27px;
    letter-spacing: 1.2px;
    color: var(--olive);
  }
</style>
</head>
<body>
<main class="canvas">
  <div class="floral-border" role="img" aria-label="Border of pink roses, pink five-petal flowers and green leafy sprigs surrounding the card"></div>

  <section class="card">
    <h1 class="headline" aria-label="Save the Date">
      <span class="save">Save</span>
      <span class="the">the</span>
      <span class="date">Date</span>
    </h1>
    <p class="tagline">for our wedding.</p>
    <p class="couple">Mona <span class="joiner">and</span> Felix</p>
    <p class="when">9<sup>th</sup> June, 2018</p>
    <p class="where">Ottawa, Ontario</p>
    <div class="divider"></div>
    <p class="note">there will be a reception in Edmonton AB September 1st<br>for those who cannot make it to Ottawa.</p>
  </section>
</main>
</body>
</html>
```